Business cards/ stationery design for a transport consultancy
Freight Lantern
Business cards/ stationery design for a transport consultancy - Consulting
Creative Brief
Use standard fonts
Use either logo font (EUROSTILE LT STD) or complimentary font type
Simple
Declan Brolly
Managing Director
Ground Floor 27/ 28 Wexholm Yard Dublin 2 Ireland
dbrolly@freightlantern.com
www.freightlantern.com
Registered office address, and company registration number will need to be included as a footer at bottom of letter template.
Emphasis on designs should be on conveying a professional image.

```html
<!DOCTYPE html>
<html lang="en">
<head>
<meta charset="utf-8">
<title>Freight Lantern – Business Card</title>
<link href="https://fonts.googleapis.com/css2?family=Michroma&family=Roboto:wght@400;700&display=swap" rel="stylesheet">
<style>
  :root {
    --backdrop: #2b2d30;
    --card-white: #ffffff;
    --blue-deep: #0b2f5c;
    --blue-mid: #14558f;
    --blue-light: #2f7fc0;
    --swoosh-grey: #6d7075;
    --text-white: #ffffff;
    --text-soft: #d6e4f2;
    --brand-blue: #1d5e9e;
  }
  * { margin: 0; padding: 0; box-sizing: border-box; }
  html, body { width: 1200px; height: 901px; overflow: hidden; }
  body {
    background: var(--backdrop);
    font-family: "Roboto", Arial, sans-serif;
    position: relative;
  }
  .card {
    position: absolute;
    left: 320px;
    width: 560px;
    height: 320px;
    border-radius: 18px;
    overflow: hidden;
  }
  .card--back {
    top: 90px;
    background: linear-gradient(135deg, var(--blue-light) 0%, var(--blue-mid) 45%, var(--blue-deep) 100%);
  }
  .card--front { top: 490px; background: var(--card-white); }
  .card__art { position: absolute; inset: 0; width: 100%; height: 100%; }

  .brand {
    position: absolute;
    display: flex;
    align-items: center;
    gap: 12px;
    font-family: "Michroma", "Arial", sans-serif;
    letter-spacing: 1px;
  }
  .brand__dot { border-radius: 50%; flex: none; }
  .card--back .brand { left: 0; right: 0; top: 118px; justify-content: center; color: var(--text-white); font-size: 26px; }
  .card--back .brand__dot { width: 30px; height: 30px; background: var(--text-white); }
  .back__web {
    position: absolute; left: 0; right: 0; bottom: 26px;
    text-align: center; color: var(--text-soft); font-size: 13px; letter-spacing: 1px;
  }

  .card--front .brand { left: 42px; top: 64px; color: var(--brand-blue); font-size: 21px; }
  .card--front .brand__dot { width: 22px; height: 22px; background: var(--brand-blue); }

  .contact {
    position: absolute; right: 30px; top: 140px;
    text-align: right; color: var(--text-white);
  }
  .contact__name { font-size: 16px; font-weight: 700; letter-spacing: 0.5px; }
  .contact__role { font-size: 10.5px; color: var(--text-soft); margin-top: 3px; }
  .contact__address { font-size: 10.5px; color: var(--text-soft); margin-top: 12px; line-height: 1.4; }
  .contact__lines { display: flex; gap: 8px; justify-content: flex-end; margin-top: 10px; }
  .contact__lines p { font-size: 10.5px; line-height: 1.5; }
  .contact__icons { display: flex; flex-direction: column; gap: 2px; padding-top: 2px; }
  .contact__icons svg { width: 12px; height: 12px; }
</style>
</head>
<body>

<section class="card card--back">
  <div class="brand"><span class="brand__dot"></span><span>Freight Lantern</span></div>
  <p class="back__web">www.freightlantern.com</p>
</section>

<section class="card card--front">
  <svg class="card__art" viewBox="0 0 560 320" preserveAspectRatio="none" aria-hidden="true">
    <defs>
      <linearGradient id="frontBlue" x1="0" y1="0" x2="1" y2="1">
        <stop offset="0" stop-color="#2f7fc0"/>
        <stop offset="0.5" stop-color="#14558f"/>
        <stop offset="1" stop-color="#0b2f5c"/>
      </linearGradient>
    </defs>
    <path class="swoosh" d="M260 0 C 430 20, 420 230, 120 320 L 160 320 C 450 230, 470 30, 300 0 Z" fill="#6d7075"/>
    <path class="blue-field" d="M300 0 L560 0 L560 320 L160 320 C 470 230, 450 20, 300 0 Z" fill="url(#frontBlue)"/>
  </svg>

  <div class="brand"><span class="brand__dot"></span><span>Freight Lantern</span></div>

  <div class="contact">
    <p class="contact__name">Declan Brolly</p>
    <p class="contact__role">Managing Director</p>
    <p class="contact__address">Ground Floor<br>27/ 28 Wexholm Yard<br>Dublin 2, Ireland</p>
    <div class="contact__lines">
      <p>+353 1 555 0147<br>+353 87 555 0382<br>dbrolly@freightlantern.com</p>
      <div class="contact__icons">
        <svg viewBox="0 0 12 12"><path d="M2 1h3l1 3-1.5 1a6 6 0 0 0 2.5 2.5L8 6l3 1v3c-5 1-10-4-9-9z" fill="#fff"/></svg>
        <svg viewBox="0 0 12 12"><rect x="3" y="0.5" width="6" height="11" rx="1" fill="none" stroke="#fff"/><circle cx="6" cy="9.5" r="0.8" fill="#fff"/></svg>
        <svg viewBox="0 0 12 12"><rect x="0.5" y="2.5" width="11" height="7" fill="none" stroke="#fff"/><path d="M0.5 2.5 6 7l5.5-4.5" fill="none" stroke="#fff"/></svg>
      </div>
    </div>
  </div>
</section>

</body>
</html>
```